KRV Holdfast Manufacturer New Web Design

We need a new theme designed for metal fastener manufacturing company, KRV Holdfast Group, a $60M division of Benmore Forge Holdings, Inc. We manufacture screw, pins and washers to industrial customers (non-Automotive) such as Tallow Appliance, Marcus Fenwold, BRU, Veltrin, etc. Our current website is www.holdfastparts.example. We would like to stick with the same logo/color scheme, however, I'm aiming to modernize the website's look and feel.

Here are some of our competitor's websites:
- https://www.torvanix.example/
- http://quellbrook.example/
- http://www.morrowbuiltcouplingworks.example/
- http://pegsandoddments.example/
- http://www.dunmerebolting.example/

Target Market(s)

We primarily want to target engineers working in the following markets:
- Appliance (Tallow Appliance, Kelvanor)
- Ag (Fenwold, BRU)
- Recreational Vehicle (Veltrin, Briar Fox)
- Outdoor Power (Oldmeadow, Vexa)

We secondarily want to target buyers working at the above markets as well as buyers at Fastener distributors such as Boltrin, Provision Dynamics, Hollis Parfet.

Industry/Entity Type

Metal Forging

Number of Pages Required

1 page

Requirements
Must have
• For products: "Threaded" product as the primary focus. "Pins" product is the secondary focus, followed by all others.
• Please use same logo and color scheme as I do not plan to change.
Nice to have
• Highlight our featured proprietary products (pamphlets attached). KRV Holdfast's KIN-V, LumDrive, Holdfast Spiral, Pelmont.

```html
<!DOCTYPE html>
<html lang="en">
<head>
<meta charset="utf-8">
<title>KRV Holdfast Group</title>
<link rel="stylesheet" href="https://fonts.googleapis.com/css2?family=Open+Sans:wght@300;400;600&family=Tinos&display=swap">
<style>
  :root {
    --navy: #14225a;
    --deep-blue: #1a3f86;
    --mid-blue: #1f6fae;
    --cyan: #2cc0dc;
    --brand-green: #2aa437;
    --heading-green: #2f9a3c;
    --white: #ffffff;
    --ink: #333333;
    --badge-red: #8e1b2c;
  }
  * { margin: 0; padding: 0; box-sizing: border-box; }
  html, body { width: 1200px; height: 750px; overflow: hidden; background: var(--white); }
  .page { position: relative; width: 1200px; height: 750px; overflow: hidden; font-family: "Open Sans", sans-serif; }

  .hero {
    position: absolute; inset: 0 0 auto 0; height: 570px;
    clip-path: polygon(0 0, 100% 0, 100% 497px, 0 569px);
  }
  .hero-backdrop {
    position: absolute; inset: 0;
    background:
      radial-gradient(ellipse 420px 300px at 62% 35%, rgba(44,192,220,.85), transparent 70%),
      radial-gradient(ellipse 260px 240px at 8% 70%, rgba(31,111,174,.7), transparent 70%),
      linear-gradient(135deg, var(--navy) 0%, var(--deep-blue) 45%, var(--mid-blue) 65%, var(--navy) 100%);
  }

  .site-header { position: absolute; top: 0; left: 0; right: 0; height: 80px; }
  .brand { position: absolute; left: 108px; top: 18px; display: flex; flex-direction: column; }
  .brand-name { display: flex; align-items: center; gap: 8px; color: var(--cyan); font-size: 24px; font-weight: 400; line-height: 1; }
  .brand-dot { width: 30px; height: 30px; border-radius: 50%; background: var(--white); display: inline-block; }
  .brand-tagline { margin-left: 38px; margin-top: 4px; color: var(--white); font-size: 8px; letter-spacing: .5px; }

  .main-nav { position: absolute; top: 32px; left: 513px; display: flex; gap: 15px; }
  .main-nav a { color: var(--white); text-decoration: none; font-size: 15px; font-weight: 600; letter-spacing: -.2px; }
  .main-nav a.is-current { color: var(--brand-green); border-bottom: 2px solid var(--brand-green); }

  .about { position: absolute; top: 176px; left: 0; right: 0; text-align: center; }
  .about-title { font-family: "Tinos", serif; font-weight: 400; font-size: 44px; color: var(--white); line-height: 1; margin-left: 10px; }
  .about-title .accent { color: var(--heading-green); }
  .about-text {
    width: 520px; margin: 22px 0 0 361px; text-align: left;
    font-family: "Tinos", serif; font-size: 21px; line-height: 26px; color: var(--white);
  }
  .cta {
    position: absolute; left: 486px; top: 358px; width: 256px; height: 41px;
    background: var(--brand-green); color: var(--white); text-decoration: none;
    font-size: 19px; font-weight: 400; display: flex; align-items: center; justify-content: center; letter-spacing: -.3px;
  }

  .connector { position: absolute; left: 598px; top: 471px; width: 2px; height: 72px; background: var(--brand-green); }

  .anniversary-mark {
    position: absolute; left: 514px; top: 545px; width: 160px; height: 112px;
    background: linear-gradient(160deg, var(--badge-red), #6e1222); border-radius: 6px;
  }

  .slogan { position: absolute; top: 664px; left: 0; right: 0; text-align: center; color: var(--ink); font-weight: 400; font-size: 32px; line-height: 32px; letter-spacing: .3px; }
  .slogan span { display: block; margin-left: 10px; }
</style>
</head>
<body>
<div class="page">
  <section class="hero">
    <div class="hero-backdrop" role="img" aria-label="Low-poly faceted background in navy, blue and cyan"></div>

    <header class="site-header">
      <div class="brand">
        <div class="brand-name"><span class="brand-dot"></span>Holdfast group</div>
        <div class="brand-tagline">SCREWS • PINS • WASHERS • SPECIALS</div>
      </div>
      <nav class="main-nav">
        <a href="#" class="is-current">HOME</a>
        <a href="#">Products</a>
        <a href="#">Capabilities</a>
        <a href="#">Engineering</a>
        <a href="#">Quality</a>
        <a href="#">About Us</a>
        <a href="#">Contact Us</a>
      </nav>
    </header>

    <div class="about">
      <h1 class="about-title">About <span class="accent">US</span></h1>
      <p class="about-text">KRV Holdfast Group, a $60M division of Benmore Forge Holdings, Inc. We manufacture screw, pins and washers to industrial customers (non-Automotive) such as Tallow Appliance, Marcus Fenwold, BRU, Veltrin, etc.</p>
    </div>
    <a href="#" class="cta">SEE OUR PRODUCTS</a>
  </section>

  <div class="connector"></div>
  <div class="anniversary-mark" role="img" aria-label="Hand-lettered 100 years of excellence anniversary mark"></div>

  <h2 class="slogan"><span>Simple Ideas</span><span>Help the Industry Take Off…</span></h2>
</div>
</body>
</html>
```